Art Business Needs a Wordpress Theme

I need a Wordpress theme for my company, Fen Ru Haven. Fen Ru stands for Love, Local and the company's focus is to increase awareness of local art and artists. The site will have a blog with posts that showcase local art, art how-to techniques, featured artists and art events. These could be broken down into separate pages or just kept within the homepage. I have a logo that I would like to incorporate. The only request I will make about the layout is that it can feature pictures prominently. Eventually with the help of a Pledgewell campaign I would like to turn the site into an upscale e-commerce platform for member artists of the site. The blog that you are designing will be built on as the business grows into its full vision.

Target Market(s)

Young professionals, Art fans and home designers

Industry/Entity Type

Business

Number of Pages Required

3 page

Font styles to use
Sans Serif

Colors
eda3c7
e667a6
e34197
f59195
f04a50
f68d4d
f37122

Requirements
Must have
• An about page and a contact page. I would like it if the logo was featured on the top left of the screen along with the words Love. Local. Art.
Nice to have
• Perhaps if possible it would be cool to have a way for people to enter their email if they were interested in joining a mailing list or having the Social media information displayed on a sidebar.

```html
<!DOCTYPE html>
<html lang="en">
<head>
<meta charset="utf-8">
<title>Fen Ru Haven – Blog</title>
<link href="https://fonts.googleapis.com/css2?family=Open+Sans:wght@400;600;700&family=Ubuntu:wght@400;500;700&display=swap" rel="stylesheet">
<style>
:root{
  --pink:#e34197;
  --pink-soft:#e667a6;
  --pink-pale:#eda3c7;
  --coral:#f04a50;
  --footer:#ef4d66;
  --footer-light:#f47c8e;
  --dark:#2f2f2f;
  --text:#666;
  --muted:#999;
  --line:#e3e3e3;
}
*{box-sizing:border-box;margin:0;padding:0}
html,body{width:667px;height:1200px;overflow:hidden}
body{font-family:"Open Sans",Arial,sans-serif;color:var(--text);background:#fff;position:relative;font-size:7px;line-height:1.45}
.topbar{height:18px;background:var(--dark);color:#ccc;font-size:5.5px;display:flex;align-items:center;justify-content:space-between;padding:0 55px}
.topbar .follow{display:flex;align-items:center;gap:4px;letter-spacing:.5px}
.topbar .dot{width:9px;height:9px;border-radius:2px;background:#555}
.topbar .dot.on{background:var(--coral)}
.header{height:67px;display:flex;align-items:center;justify-content:space-between;padding:0 55px;border-bottom:1px solid var(--line)}
.brand{display:flex;flex-direction:column;align-items:center;gap:3px}
.brand .mark{width:32px;height:32px;border-radius:50%;background:var(--pink)}
.brand .name{font-family:"Ubuntu",sans-serif;font-size:8px;color:var(--pink);font-weight:500}
.nav{display:flex;gap:0}
.nav a{display:block;padding:0 10px;border-left:1px solid var(--line);text-decoration:none;font-family:"Ubuntu",sans-serif;color:#333;font-size:9px;font-weight:500;line-height:1.1}
.nav a:first-child{border-left:0}
.nav a small{display:block;font-family:"Open Sans",sans-serif;font-size:5.5px;color:var(--muted);font-weight:400}
.titleband{height:53px;display:flex;align-items:center;justify-content:space-between;padding:0 55px;border-bottom:1px solid var(--line)}
.titleband h1{font-family:"Ubuntu",sans-serif;font-size:25px;font-weight:400;color:var(--pink-soft);line-height:1}
.titleband p{font-size:5.5px;color:var(--muted)}
.newsletter{display:flex;align-items:center;gap:6px}
.newsletter label{font-family:"Ubuntu",sans-serif;font-size:9px;color:#333}
.newsletter .field{width:70px;height:15px;background:var(--coral);color:#fff;font-size:5.5px;padding:4px}
.newsletter .btn{height:15px;background:var(--dark);color:#fff;font-size:6px;padding:3px 7px}
.main{position:absolute;top:138px;left:55px;width:345px}
.post{height:250px;padding-top:0}
.post .photo{height:124px;border:4px solid #fff;box-shadow:0 1px 4px rgba(0,0,0,.3)}
.post .head{display:flex;gap:8px;margin-top:8px}
.date{width:23px;height:23px;border-radius:50%;background:var(--pink);color:#fff;text-align:center;font-size:9px;font-weight:700;line-height:1;padding-top:3px;flex:none}
.date small{display:block;font-size:5px;font-weight:400}
.post h2{font-family:"Ubuntu",sans-serif;font-size:10px;font-weight:400;color:var(--pink);text-transform:uppercase}
.meta{font-size:5px;color:var(--muted)}
.post .excerpt{margin:5px 0 0 31px;font-size:5.5px;line-height:1.6}
.post .tools{margin:6px 0 0 31px;display:flex;justify-content:space-between;align-items:center}
.icons{display:flex;gap:4px}
.icons span{width:7px;height:7px;background:#bbb;border-radius:1px}
.more{width:8px;height:8px;background:var(--pink)}
.pager{position:absolute;top:895px;left:327px;width:11px;height:11px;border-radius:50%;background:var(--dark)}
.sidebar{position:absolute;top:138px;left:445px;width:178px}
.sidebar h3{font-family:"Ubuntu",sans-serif;font-size:9px;font-weight:500;color:#333;padding-bottom:4px;border-bottom:1px solid var(--line);margin-bottom:6px}
.tweet{display:flex;gap:6px;margin-bottom:6px;font-size:5px;line-height:1.5}
.tweet .bird{width:11px;height:11px;border-radius:50%;background:var(--pink-pale);flex:none}
.tweet em{color:var(--pink);font-style:normal}
.comment{border:1px solid var(--line);padding:5px 7px;font-size:5px;margin-bottom:10px}
.comment cite{display:block;text-align:right;color:var(--pink);font-style:normal;margin-top:2px}
.widget{margin-bottom:14px}
.recent{display:flex;gap:6px;margin-bottom:6px}
.recent .thumb{width:30px;height:22px;flex:none}
.recent p{font-size:5px}
.recent b{color:var(--pink);font-weight:400}
.list li{list-style:none;font-size:5.5px;padding:2.5px 0;border-bottom:1px solid #f1f1f1;display:flex;align-items:center;gap:5px}
.list li::before{content:"";width:6px;height:4px;background:var(--pink-pale)}
.list li.active{color:var(--pink)}
.footer{position:absolute;top:915px;left:0;width:667px;height:265px;background:var(--footer);color:#fff;display:flex;gap:38px;padding:18px 55px 0}
.footer h4{font-family:"Ubuntu",sans-serif;font-size:9px;font-weight:500;text-transform:uppercase;margin-bottom:8px;letter-spacing:.5px}
.col{width:165px;font-size:5px}
.grid{display:grid;grid-template-columns:repeat(3,1fr);gap:5px;margin-top:8px}
.grid span{height:36px;background:var(--footer-light)}
.btn-dark{display:inline-block;background:var(--dark);color:#fff;font-size:5px;padding:3px 8px;margin:8px 0 0 60px}
.form .row{display:flex;align-items:center;margin-bottom:5px;gap:6px}
.form .row i{font-style:normal;width:30px;color:#fff;font-size:5px}
.form .box{background:var(--footer-light);height:10px;flex:1}
.form .area{background:var(--footer-light);height:60px;margin-bottom:6px}
.form .send{text-align:center;font-size:5.5px}
.fpost{display:flex;gap:6px;margin-bottom:9px}
.fpost .thumb{width:40px;height:30px;border:2px solid #fff;flex:none}
.bottombar{position:absolute;top:1180px;left:0;width:667px;height:20px;background:var(--dark);color:#ccc;font-size:5.5px;display:flex;align-items:center;justify-content:space-between;padding:0 55px}
.bottombar nav{display:flex;gap:12px}
</style>
</head>
<body>
<div class="topbar">
  <span>This is a notification bar. You can use it to give your visitors useful news.</span>
  <div class="follow">FOLLOW US ON <span class="dot on"></span><span class="dot"></span><span class="dot"></span></div>
</div>

<header class="header">
  <div class="brand"><span class="mark"></span><span class="name">Fen Ru Haven</span></div>
  <nav class="nav">
    <a>HOME<small>Start here</small></a>
    <a>FEATURES<small>What we do</small></a>
    <a>PORTFOLIO<small>Our artists</small></a>
    <a>BLOG<small>Latest news</small></a>
    <a>CONTACT<small>Say hello</small></a>
  </nav>
</header>

<section class="titleband">
  <div><h1>BLOG</h1><p>Love. Local. Art. News, events and artist stories.</p></div>
  <div class="newsletter"><label>Newsletter</label><span class="field">Your email</span><span class="btn">Subscribe</span></div>
</section>

<main class="main">
  <article class="post">
    <div class="photo" role="img" aria-label="Close-up of a paintbrush on a colourful palette" style="background:linear-gradient(120deg,#6f8fa8,#d9a24a 40%,#c7433d 70%,#5d7a3b)"></div>
    <div class="head"><div class="date">20<small>JUN</small></div><div><h2>My first very long blog post title</h2><p class="meta">By: admin · Written in: Art Events · 11 comments</p></div></div>
    <p class="excerpt">Local painters gather each month to share new work, swap techniques and talk about the stories behind every canvas. Join us for the next open studio evening and meet the makers in person.</p>
    <div class="tools"><div class="icons"><span></span><span></span><span></span><span></span><span></span></div><span class="more"></span></div>
  </article>
  <article class="post">
    <div class="photo" role="img" aria-label="Black and white photograph of roses" style="background:linear-gradient(135deg,#d8d8d8,#555 55%,#222)"></div>
    <div class="head"><div class="date">20<small>JUN</small></div><div><h2>My first very long blog post title</h2><p class="meta">By: admin · Written in: How-To · 11 comments</p></div></div>
    <p class="excerpt">A simple guide to shooting still life in monochrome, from choosing light to framing petals. Our featured artist explains each step so you can try it at home this weekend.</p>
    <div class="tools"><div class="icons"><span></span><span></span><span></span><span></span><span></span></div><span class="more"></span></div>
  </article>
  <article class="post">
    <div class="photo" role="img" aria-label="Watercolour painting of a colourful street with flowers" style="background:linear-gradient(120deg,#b8a9d6,#e9c2c9 40%,#9fc68f 70%,#d7b66c)"></div>
    <div class="head"><div class="date">20<small>JUN</small></div><div><h2>My first very long blog post title</h2><p class="meta">By: admin · Written in: Featured Artists · 11 comments</p></div></div>
    <p class="excerpt">Meet the watercolour artist who paints our neighbourhood streets in soft spring tones. She shares her favourite papers, brushes and the corners of town that inspire her most.</p>
    <div class="tools"><div class="icons"><span></span><span></span><span></span><span></span><span></span></div><span class="more"></span></div>
  </article>
</main>
<span class="pager"></span>

<aside class="sidebar">
  <section class="widget">
    <h3>Latest Tweets</h3>
    <div class="tweet"><span class="bird"></span><p>Open studio night is back this Friday, bring a friend and meet local makers. <em>2 days ago</em></p></div>
    <div class="tweet"><span class="bird"></span><p>New how-to post on layering acrylics is live on the blog now. <em>3 days ago</em></p></div>
    <div class="tweet"><span class="bird"></span><p>Thank you to everyone who visited the spring art walk downtown. <em>5 days ago</em></p></div>
  </section>
  <section class="widget">
    <h3>Latest Comments</h3>
    <div class="comment">Lovely write-up, I visited the gallery last week and the new pieces are stunning in person.<cite>by Maren on Spring Walk post</cite></div>
    <div class="comment">Great tips on brushes, I will try the wet layering method on my next canvas.<cite>by Teo on How-To post</cite></div>
  </section>
  <section class="widget">
    <h3>Latest from our Blog</h3>
    <div class="recent"><span class="thumb" role="img" aria-label="Colourful painting thumbnail" style="background:linear-gradient(#7aa0c8,#e0b05a)"></span><p><b>This is a sample Post 1</b><br>A short note about this week in local art.</p></div>
    <div class="recent"><span class="thumb" role="img" aria-label="Red flower photo thumbnail" style="background:linear-gradient(#c0392b,#5a1a12)"></span><p><b>This is a sample Post 2</b><br>A short note about this week in local art.</p></div>
    <div class="recent"><span class="thumb" role="img" aria-label="Black and white photo thumbnail" style="background:linear-gradient(#ccc,#333)"></span><p><b>This is a sample Post 3</b><br>A short note about this week in local art.</p></div>
  </section>
  <section class="widget">
    <h3>Blog Categories</h3>
    <ul class="list"><li>Blog Categories 1 (3)</li><li>Blog Categories 2 (5)</li><li class="active">Blog Categories 3 (8)</li><li>Blog Categories 4 (12)</li><li>Blog Categories 5 (4)</li></ul>
  </section>
  <section class="widget">
    <h3>Archives</h3>
    <ul class="list"><li>January 2012 (3)</li><li>December 2011 (5)</li><li class="active">November 2011 (7)</li><li>October 2011 (4)</li><li>September 2011 (6)</li><li>August 2011 (2)</li></ul>
  </section>
</aside>

<footer class="footer">
  <div class="col">
    <h4>Snapline Gallery</h4>
    <p>Recent snapshots from studio visits, art walks and gallery openings across town.</p>
    <div class="grid" role="img" aria-label="Grid of gallery photos"><span></span><span></span><span></span><span></span><span></span><span></span><span></span><span></span><span></span></div>
    <span class="btn-dark">View More</span>
  </div>
  <div class="col form">
    <h4>Get in Touch</h4>
    <div class="row"><i>Name</i><span class="box"></span></div>
    <div class="row"><i>Email</i><span class="box"></span></div>
    <div class="row"><i>Website</i><span class="box"></span></div>
    <div class="area"></div>
    <p class="send">Send Message</p>
  </div>
  <div class="col">
    <h4>Latest Posts</h4>
    <div class="fpost"><span class="thumb" role="img" aria-label="Painting thumbnail" style="background:linear-gradient(#7aa0c8,#e0b05a)"></span><p>This is a sample Post 1<br>A short note about this week in local art and artists.</p></div>
    <div class="fpost"><span class="thumb" role="img" aria-label="Flower thumbnail" style="background:linear-gradient(#c0392b,#5a1a12)"></span><p>This is a sample Post 2<br>A short note about this week in local art and artists.</p></div>
    <div class="fpost"><span class="thumb" role="img" aria-label="Colourful artwork thumbnail" style="background:linear-gradient(#6bb0d8,#e36b8f)"></span><p>This is a sample Post 3<br>A short note about this week in local art and artists.</p></div>
  </div>
</footer>

<div class="bottombar">
  <span>© 2011 www.companyname.com</span>
  <nav><span>HOME</span><span>FEATURES</span><span>CONTACT</span><span>FORUM</span></nav>
</div>
</body>
</html>
```